we need a design for Water Bottle Lable Wrap
The product is called Corvane Water is a restructured water. its a very healthy and rejuvenating water
we were looking at using as a tag ling Restore, Recover, Rejuvenate.

```html
<!DOCTYPE html>
<html lang="en">
<head>
<meta charset="utf-8">
<title>Corvane Water – Label Wrap</title>
<link href="https://fonts.googleapis.com/css2?family=Montserrat:wght@500;600;900&display=swap" rel="stylesheet">
<style>
  :root {
    --page-bg: #f4f5f6;
    --sky: #64cbf1;
    --lake: #19afd6;
    --snow: #ffffff;
    --earth: #7a4f2c;
    --forest: #2e6a33;
    --pill-text: #19afd6;
    --white: #ffffff;
  }
  * { margin: 0; padding: 0; box-sizing: border-box; }
  html, body {
    width: 1200px;
    height: 1113px;
    overflow: hidden;
    background: var(--page-bg);
    font-family: "Montserrat", sans-serif;
  }
  .label-wrap {
    position: absolute;
    left: 118px;
    top: 40px;
    width: 963px;
    height: 1033px;
    background: var(--lake);
    overflow: hidden;
  }
  .landscape {
    position: absolute;
    left: 0;
    top: 0;
    width: 100%;
    height: 519px;
    background: linear-gradient(
      to bottom,
      var(--sky) 0%,
      var(--sky) 8%,
      var(--snow) 22%,
      var(--snow) 30%,
      var(--earth) 50%,
      #8b5e38 66%,
      var(--forest) 80%,
      var(--forest) 100%
    );
  }
  .brand {
    position: absolute;
    left: 0;
    width: 100%;
    text-align: center;
    color: var(--white);
    line-height: 1;
  }
  .brand-name {
    top: 576px;
    font-size: 76px;
    font-weight: 500;
    letter-spacing: 1px;
  }
  .brand-product {
    top: 664px;
    font-size: 84px;
    font-weight: 900;
    letter-spacing: 0.5px;
  }
  .category-pill {
    position: absolute;
    left: 249px;
    top: 769px;
    width: 464px;
    height: 58px;
    background: var(--white);
    border-radius: 30px 12px 30px 12px;
    color: var(--pill-text);
    font-size: 27px;
    font-weight: 600;
    letter-spacing: 0.5px;
    display: flex;
    align-items: center;
    justify-content: center;
  }
  .benefits {
    position: absolute;
    left: 345px;
    top: 846px;
    list-style: none;
    color: var(--white);
    font-size: 31px;
    font-weight: 600;
    letter-spacing: 0.5px;
    line-height: 41px;
  }
  .benefits li {
    display: flex;
    align-items: center;
    gap: 10px;
  }
  .tick { width: 26px; height: 22px; flex: none; }
</style>
</head>
<body>
  <main class="label-wrap">
    <div class="landscape" role="img" aria-label="Flat illustration of snow-capped mountains with brown slopes, pine forest and a stream flowing into a lake"></div>

    <h1 class="brand brand-name">CORVANE</h1>
    <p class="brand brand-product">WATER</p>

    <div class="category-pill">RESTRUCTURED WATER</div>

    <ul class="benefits">
      <li><svg class="tick" viewBox="0 0 26 22" aria-hidden="true"><path d="M2 12 L9 19 L24 3" fill="none" stroke="#fff" stroke-width="4" stroke-linecap="round" stroke-linejoin="round"/></svg>RESTORE</li>
      <li><svg class="tick" viewBox="0 0 26 22" aria-hidden="true"><path d="M2 12 L9 19 L24 3" fill="none" stroke="#fff" stroke-width="4" stroke-linecap="round" stroke-linejoin="round"/></svg>RECOVER</li>
      <li><svg class="tick" viewBox="0 0 26 22" aria-hidden="true"><path d="M2 12 L9 19 L24 3" fill="none" stroke="#fff" stroke-width="4" stroke-linecap="round" stroke-linejoin="round"/></svg>REJUVENATE</li>
    </ul>
  </main>
</body>
</html>
```